Business Card Design

It is an assisted living facility. I wanted the name to reflect that we are a step above other facilities; i.e., professionally decorated rooms, cloth napkins, family dinners, etc. My motto is: A WARM WELCOME AWAITS YOU DAILY! Also, I have thought about having a house held with the "Hands" and the motto around it but I have seen that logo used other places. In other words, HELP!

I do not have a photo yet, but the photographer is coming next week. I would like the back of the card to have a picture of the facility.

Industry/Entity Type

Business

Contact Information for Business Card

BRIGHT MEADOW ASSISTED LIVING, LLC, 2938 Quillmont Dr., FL 33482-7261
Phone: (555) 214-6037; Fax: (555)
Linda Pruett, Owner/Administrator

```html
<!DOCTYPE html>
<html lang="en">
<head>
<meta charset="utf-8">
<title>Linda Pruett – Bright Meadow Assisted Living</title>
<link rel="stylesheet" href="https://fonts.googleapis.com/css2?family=Arimo&family=Playfair+Display:wght@400&display=swap">
<style>
  :root {
    --ink-blue: #2b5b86;
    --ink-green: #2f4a30;
    --bg-light: #f7f7f7;
    --bg-mid: #e4e4e4;
    --bg-soft: #ededed;
  }
  * { margin: 0; padding: 0; box-sizing: border-box; }
  html, body { width: 1200px; height: 702px; overflow: hidden; background: #ffffff; }
  .card {
    position: relative;
    width: 1200px;
    height: 702px;
    overflow: hidden;
    font-family: "Arimo", Arial, sans-serif;
  }
  .card-backdrop {
    position: absolute;
    inset: 0;
    background:
      radial-gradient(ellipse at 30% 42%, var(--bg-light) 0%, rgba(247,247,247,0) 45%),
      linear-gradient(135deg, var(--bg-mid) 0%, var(--bg-soft) 30%, var(--bg-light) 55%, var(--bg-soft) 80%, var(--bg-mid) 100%);
  }
  .holder-name {
    position: absolute;
    left: 690px;
    top: 44px;
    font-family: "Playfair Display", Georgia, serif;
    font-weight: 400;
    font-size: 58px;
    letter-spacing: 5px;
    color: var(--ink-blue);
    white-space: nowrap;
  }
  .contact-row {
    position: absolute;
    left: 634px;
    display: flex;
    align-items: center;
    gap: 42px;
  }
  .contact-row--phone { top: 206px; }
  .contact-row--fax { top: 311px; }
  .contact-icon { width: 60px; height: 60px; flex: none; }
  .contact-number {
    font-size: 37px;
    letter-spacing: 1.5px;
    color: var(--ink-blue);
  }
  .brand-name {
    position: absolute;
    left: 120px;
    top: 268px;
    width: 280px;
    text-align: center;
    font-family: "Playfair Display", Georgia, serif;
    font-size: 36px;
    line-height: 1.2;
    color: var(--ink-blue);
  }
  .tagline {
    position: absolute;
    left: 68px;
    top: 488px;
    font-family: "Arimo", Arial, sans-serif;
    font-size: 15px;
    letter-spacing: 1.6px;
    color: var(--ink-green);
    white-space: nowrap;
  }
  .address-row {
    position: absolute;
    left: 60px;
    top: 603px;
    display: flex;
    align-items: center;
    gap: 18px;
  }
  .address-icon { width: 44px; height: 44px; flex: none; }
  .address-text {
    font-size: 22.5px;
    letter-spacing: 1.6px;
    color: var(--ink-blue);
    white-space: nowrap;
  }
</style>
</head>
<body>
<main class="card">
  <div class="card-backdrop" role="img" aria-label="Soft grey diamond pattern background"></div>

  <h1 class="holder-name">Linda Pruett</h1>

  <div class="contact-row contact-row--phone">
    <svg class="contact-icon" viewBox="0 0 60 60" aria-label="Phone">
      <defs>
        <radialGradient id="iconGloss" cx="50%" cy="30%" r="70%">
          <stop offset="0" stop-color="#ffffff"/>
          <stop offset="0.55" stop-color="#dcdcdc"/>
          <stop offset="1" stop-color="#8e8e8e"/>
        </radialGradient>
      </defs>
      <circle cx="30" cy="30" r="28" fill="url(#iconGloss)"/>
      <rect x="22" y="15" width="16" height="30" rx="2.5" fill="#3d3d3d"/>
      <rect x="24.5" y="19" width="11" height="20" fill="#e9e9e9"/>
      <rect x="28" y="41" width="4" height="1.6" fill="#e9e9e9"/>
    </svg>
    <span class="contact-number">(555) 214-6037</span>
  </div>

  <div class="contact-row contact-row--fax">
    <svg class="contact-icon" viewBox="0 0 60 60" aria-label="Fax">
      <defs>
        <radialGradient id="iconGlossDark" cx="50%" cy="25%" r="75%">
          <stop offset="0" stop-color="#e6e6e6"/>
          <stop offset="0.5" stop-color="#9a9a9a"/>
          <stop offset="1" stop-color="#4a4a4a"/>
        </radialGradient>
      </defs>
      <circle cx="30" cy="30" r="28" fill="url(#iconGlossDark)"/>
      <rect x="21" y="14" width="18" height="9" fill="#3a3a3a"/>
      <rect x="13" y="22" width="34" height="16" rx="3" fill="#3a3a3a"/>
      <rect x="20" y="32" width="20" height="14" fill="#f2f2f2" stroke="#3a3a3a" stroke-width="1.5"/>
      <rect x="23" y="36" width="14" height="1.8" fill="#3a3a3a"/>
      <rect x="23" y="40" width="14" height="1.8" fill="#3a3a3a"/>
    </svg>
    <span class="contact-number">(555) 214-6037</span>
  </div>

  <p class="brand-name">Bright Meadow</p>

  <p class="tagline">A WARM WELCOME AWAITS YOU DAILY!</p>

  <div class="address-row">
    <svg class="address-icon" viewBox="0 0 44 44" aria-label="Address">
      <defs>
        <radialGradient id="pinGloss" cx="50%" cy="30%" r="70%">
          <stop offset="0" stop-color="#ffffff"/>
          <stop offset="0.6" stop-color="#d6d6d6"/>
          <stop offset="1" stop-color="#909090"/>
        </radialGradient>
      </defs>
      <circle cx="22" cy="22" r="21" fill="url(#pinGloss)"/>
      <path d="M22 9c-5.2 0-9 3.8-9 8.8 0 6.4 9 16.7 9 16.7s9-10.3 9-16.7C31 12.8 27.2 9 22 9z" fill="#444"/>
      <circle cx="22" cy="18" r="3.4" fill="#dcdcdc"/>
    </svg>
    <span class="address-text">BRIGHT MEADOW ASSISTED LIVING, LLC,2938 Quillmont Dr., FL 33482-7261</span>
  </div>
</main>
</body>
</html>
```